Electrical Product Brochure Design

We have 15 electricians on the road and want to create a product brochure for them to show residential clients. I have attached all the product images in high res to be used and some images of our company and logo. I have also attached a previous product brochure that was designed which we don't want to use/has been edited. Additionally there is a Word document with the content that is needed.

Please create the brochure as a double sided A4 brochure.
Updates

Hi, Thank you for your designs. Please see the updated brief including ensuring the design is a double sided A4 flyer. Please ensure all products from the product brochure content are used on the design and all content. Please ensure Travik's contact information is used as well. Please ensure you see the updated brief for new product images I have now been able to upload as well as a few options for images of our tradespeople that can be used. Thank you.

Target Market(s)

Homeowners

Industry/Entity Type

Electrical

Font styles to use
Sans Serif

Colors
0255a3
fbed22
ec1f27

Requirements
Must have
• Travik colours including mainly blue, but also red and a bit of yellow.
• Travik's contact information including website, phone, email, and PO Box address.
• Each product's image with the content listed next to the image.
Nice to have
• If the four types of fan images could be used, and listed as one product.
• If you could also use images of our tradespeople attached as well?

```html
<!DOCTYPE html>
<html lang="en">
<head>
<meta charset="utf-8">
<title>Travik Electrical Services – Product Flyer</title>
<link rel="stylesheet" href="https://fonts.googleapis.com/css2?family=Tinos:wght@400;700&family=Open+Sans:wght@400;600&display=swap">
<style>
:root{
  --navy:#1d2a6e;
  --brand-blue:#0255a3;
  --brand-red:#ec1f27;
  --brand-yellow:#fbed22;
  --heading-blue:#263a8f;
  --rule-pink:#f2b8c0;
  --ink:#1a1a1a;
  --paper:#ffffff;
  --photo-grey:#e6e8ec;
  --photo-warm:#efe6cf;
}
*{box-sizing:border-box;margin:0;padding:0}
html,body{width:849px;height:1200px;overflow:hidden;background:var(--paper)}
.flyer{position:relative;width:849px;height:1200px;overflow:hidden;background:var(--paper);font-family:"Open Sans",Arial,sans-serif;color:var(--ink)}
.abs{position:absolute}
.swoosh{position:absolute;left:0;width:849px}
.swoosh--top{top:0;height:100px}
.swoosh--bottom{bottom:0;height:100px}
.brand{left:28px;top:31px;width:242px;height:76px;border:1.5px solid var(--navy);background:var(--paper);display:flex;align-items:center;justify-content:center;gap:12px}
.brand__mark{width:14px;height:14px;background:var(--brand-yellow)}
.brand__name{font-family:"Open Sans",Arial,sans-serif;font-weight:600;font-size:34px;letter-spacing:5px;color:var(--brand-blue)}
.contact{position:absolute;left:300px;top:80px;width:520px;display:flex;flex-wrap:wrap;justify-content:flex-end;column-gap:18px;row-gap:3px;font-size:10.5px;font-weight:600;color:var(--navy)}
.contact__item{display:flex;align-items:center;gap:5px;white-space:nowrap}
.contact__icon{width:12px;height:12px;flex:none}
.rule{position:absolute;left:0;width:849px;height:1.5px;background:var(--rule-pink)}
.divider{position:absolute;left:345px;top:124px;width:1.5px;height:328px;background:var(--rule-pink)}
.label{position:absolute;background:var(--navy);color:#fff;font-family:"Tinos","Times New Roman",serif;font-size:19px;letter-spacing:.5px;display:flex;align-items:center;padding-left:22px;border-right:5px solid var(--brand-red)}
.label--center{justify-content:center;padding-left:0}
.photo{position:absolute;border-radius:4px}
.copy{position:absolute}
.copy h3{font-family:"Tinos","Times New Roman",serif;font-weight:400;font-size:18px;color:var(--heading-blue);border-bottom:1.3px solid var(--ink);padding-bottom:1px;margin-bottom:5px;line-height:1.1}
.copy p{font-size:11.2px;font-weight:600;line-height:1.72}
.copy .gap{height:12px}
</style>
</head>
<body>
<main class="flyer">

  <svg class="swoosh swoosh--top" viewBox="0 0 849 100" preserveAspectRatio="none" aria-hidden="true">
    <defs>
      <linearGradient id="swTop" x1="0" y1="0" x2="1" y2="0">
        <stop offset="0" stop-color="#0255a3" stop-opacity="0"/>
        <stop offset=".45" stop-color="#0255a3" stop-opacity=".55"/>
        <stop offset="1" stop-color="#1d2a6e"/>
      </linearGradient>
    </defs>
    <path d="M250 60 C450 30 650 10 849 0 L849 46 C650 30 460 45 250 60 Z" fill="url(#swTop)"/>
    <path d="M260 70 C480 40 680 35 849 50" fill="none" stroke="#0255a3" stroke-opacity=".35" stroke-width="1.5"/>
    <path d="M300 62 C500 20 700 12 849 14" fill="none" stroke="#0255a3" stroke-opacity=".4" stroke-width="1"/>
  </svg>

  <div class="abs brand"><span class="brand__mark"></span><span class="brand__name">TRAVIK</span></div>

  <div class="contact">
    <span class="contact__item">
      <svg class="contact__icon" viewBox="0 0 12 12" aria-hidden="true"><path d="M2.5 1 L4.5 1 L5.3 3.4 L4 4.4 C4.6 5.8 6.2 7.4 7.6 8 L8.6 6.7 L11 7.5 L11 9.5 C11 10.4 10.3 11 9.5 11 C5 10.7 1.3 7 1 2.5 C1 1.7 1.6 1 2.5 1 Z" fill="var(--brand-red)"/></svg>
      (03) 5550 1842
    </span>
    <span class="contact__item">
      <svg class="contact__icon" viewBox="0 0 12 12" aria-hidden="true"><rect x="1" y="2.5" width="10" height="7" rx="1" fill="none" stroke="var(--brand-red)" stroke-width="1.3"/><path d="M1.5 3 L6 6.5 L10.5 3" fill="none" stroke="var(--brand-red)" stroke-width="1.3"/></svg>
      office@travikelectrical.com.au
    </span>
    <span class="contact__item">
      <svg class="contact__icon" viewBox="0 0 12 12" aria-hidden="true"><circle cx="6" cy="6" r="4.8" fill="none" stroke="var(--brand-red)" stroke-width="1.2"/><path d="M1.2 6 H10.8 M6 1.2 C3.8 4 3.8 8 6 10.8 M6 1.2 C8.2 4 8.2 8 6 10.8" fill="none" stroke="var(--brand-red)" stroke-width="1"/></svg>
      www.travikelectrical.com.au
    </span>
    <span class="contact__item">
      <svg class="contact__icon" viewBox="0 0 12 12" aria-hidden="true"><path d="M6 11 C3 7.5 2 5.8 2 4.3 A4 4 0 0 1 10 4.3 C10 5.8 9 7.5 6 11 Z" fill="var(--brand-red)"/><circle cx="6" cy="4.3" r="1.4" fill="#fff"/></svg>
      PO Box 418, Harlow Vale VIC 3981
    </span>
  </div>

  <div class="rule" style="top:124px"></div>
  <div class="divider"></div>

  <!-- Dimmers -->
  <div class="label label--center" style="left:82px;top:135px;width:159px;height:31px">DIMMERS</div>
  <div class="photo" role="img" aria-label="Dimmer switch product in retail packaging" style="left:85px;top:185px;width:128px;height:113px;background:linear-gradient(160deg,#d9d3e8,#efeef4)"></div>
  <div class="copy" style="left:40px;top:314px;width:251px">
    <h3>Features</h3>
    <p>Adapts lighting to brightness preference</p>
    <div class="gap"></div>
    <h3>Benefits</h3>
    <p>Creates mood lighting<br>Energy saving</p>
  </div>

  <!-- Double power point -->
  <div class="label label--center" style="left:386px;top:135px;width:402px;height:31px">DOUBLE POWER POINT WITH USBs</div>
  <div class="photo" role="img" aria-label="White double power point with two USB sockets" style="left:532px;top:192px;width:114px;height:64px;background:linear-gradient(180deg,#f4f5f6,var(--photo-grey))"></div>
  <div class="copy" style="left:376px;top:283px;width:426px">
    <h3>Features</h3>
    <p>2 x 2.1 AMP USB sockets for faster charging</p>
    <div class="gap"></div>
    <h3>Benefits</h3>
    <p>Reduces clutter and bulky chargers<br>You can charge two devices such as your smart phone and tablet at once<br>More space for other appliances to be plugged in</p>
  </div>

  <div class="rule" style="top:452px"></div>

  <!-- Quad power point -->
  <div class="label" style="left:0;top:463px;width:483px;height:34px">QUAD POWER POINT WITH USB CHARGING</div>
  <div class="photo" role="img" aria-label="White quad power point with USB charging sockets" style="left:85px;top:561px;width:220px;height:50px;background:linear-gradient(180deg,#f6f7f8,var(--photo-grey))"></div>
  <div class="copy" style="left:412px;top:514px;width:390px">
    <h3>Features</h3>
    <p>Four power points in one unit</p>
    <div class="gap"></div>
    <h3>Benefits</h3>
    <p>Makes your home neater<br>Great for when you need to plug in multiple devices or appliances<br>USB option for convenient charging and even more space saving</p>
  </div>

  <div class="rule" style="top:670px"></div>

  <!-- Heat / light / fan -->
  <div class="label" style="left:0;top:687px;width:450px;height:43px">VEXO HEAT/LIGHT/FAN – 2 AND 4 HEAT</div>
  <div class="photo" role="img" aria-label="Bathroom heat, light and fan unit with two heat lamps" style="left:64px;top:760px;width:142px;height:106px;background:radial-gradient(circle at 50% 50%,var(--photo-warm),#f3f3f1 75%)"></div>
  <div class="photo" role="img" aria-label="Bathroom heat, light and fan unit with four heat lamps" style="left:227px;top:760px;width:185px;height:106px;background:radial-gradient(circle at 50% 50%,var(--photo-warm),#f3f3f1 75%)"></div>
  <div class="copy" style="left:464px;top:749px;width:338px">
    <h3>Features</h3>
    <p>2 or 4 x heat lamps for instant heat and comfort</p>
    <div class="gap"></div>
    <h3>Benefits</h3>
    <p>Powerful extraction to prevent steam and mould build up<br>Option of 275W or 375W Heat Lamp</p>
  </div>

  <div class="rule" style="top:905px"></div>

  <!-- Ceiling fans -->
  <div class="label" style="left:0;top:916px;width:515px;height:40px">CEILING FANS (WITH AND WITHOUT LIGHT)</div>
  <div class="photo" role="img" aria-label="Four styles of ceiling fan, with and without light" style="left:92px;top:966px;width:327px;height:128px;background:linear-gradient(135deg,#eef0f3,#dcdfe4 50%,#eef0f3)"></div>
  <div class="copy" style="left:464px;top:965px;width:338px">
    <h3>Features</h3>
    <p>Energy efficient when compared with expensive air<br>conditioning costs</p>
    <div class="gap"></div>
    <h3>Benefits</h3>
    <p>Comes with or without a light<br>Available with remote control for convenience<br>Can replace an existing light fitting</p>
  </div>

  <svg class="swoosh swoosh--bottom" viewBox="0 0 849 100" preserveAspectRatio="none" aria-hidden="true">
    <defs>
      <linearGradient id="swBottom" x1="0" y1="0" x2="1" y2="0">
        <stop offset="0" stop-color="#0255a3"/>
        <stop offset=".55" stop-color="#0255a3" stop-opacity=".6"/>
        <stop offset="1" stop-color="#0255a3" stop-opacity=".15"/>
      </linearGradient>
    </defs>
    <path d="M0 30 C250 68 550 88 849 94 L849 100 L0 100 Z" fill="url(#swBottom)"/>
    <path d="M0 18 C260 58 560 78 849 84" fill="none" stroke="#1d2a6e" stroke-opacity=".5" stroke-width="1.2"/>
    <path d="M0 40 C280 72 580 86 849 90" fill="none" stroke="#fbed22" stroke-width="1.5"/>
  </svg>

</main>
</body>
</html>
```